Rural contractor needs professional informative business card

We need a business card design that looks professional but also includes information about the services that the business offers.
The business is an earthmoving and transport business. All of the services offered are listed on the old card attached.
The business is aimed at farmers so the design we are after is a classic look. The card needs to include all of the information that is listed on the old card design uploaded as an attachment. We recognize that this is a lot of information to fit on a business card but it also operates as a key marketing tool so is very important to the business.
Feel free to send me your questions.
Thanks
Reason: We are having trouble deciding between all these great designs - thank you for your efforts
We would love to see some designs using red with a little white and black. Also feel free to re-design our logo if you feel it needs to be to fit your designs. Thank you

```html
<!DOCTYPE html>
<html lang="en">
<head>
<meta charset="utf-8">
<title>RT Hadley Contracting – Business Card</title>
<link href="https://fonts.googleapis.com/css2?family=Archivo+Black&display=swap" rel="stylesheet">
<style>
  :root {
    --bg: #2b2b2b;
    --card-light: #e9e6b4;
    --card-mid: #d8d397;
    --card-dark: #c4be7c;
    --ink: #111111;
    --pill-text: #e9e6b4;
    --field-sky: #dfe3cf;
    --field-wheat: #cdbf84;
    --field-soil: #b9a96a;
  }
  * { margin: 0; padding: 0; box-sizing: border-box; }
  html, body {
    width: 1200px; height: 1000px; overflow: hidden;
    background: var(--bg);
  }
  .canvas {
    position: relative; width: 1200px; height: 1000px;
    font-family: "Archivo Black", "Arial Black", sans-serif;
    color: var(--ink);
  }
  .card {
    position: absolute; left: 310px; width: 580px; height: 340px;
    border-radius: 30px; overflow: hidden;
  }
  .card--front { top: 90px; background: linear-gradient(135deg, var(--card-light), var(--card-mid) 60%, var(--card-dark)); }
  .card--back { top: 560px; }
  .dotted {
    position: absolute; left: 0; right: 0; height: 0;
    border-top: 4px dotted var(--ink);
  }
  .business-name {
    position: absolute; left: 34px; top: 104px;
    font-size: 19px; line-height: 1; letter-spacing: 0.5px; white-space: nowrap;
  }
  .contact { position: absolute; right: 30px; top: 24px; text-align: right; }
  .contact .phone { font-size: 30px; letter-spacing: 3px; line-height: 1; }
  .contact .address { font-size: 14px; letter-spacing: 1.5px; line-height: 1.3; margin-top: 4px; }
  .name-pill {
    position: absolute; left: 50%; top: 148px; transform: translateX(-50%);
    background: var(--ink); color: var(--pill-text);
    border-radius: 30px; padding: 10px 34px;
    font-size: 22px; letter-spacing: 3px; white-space: nowrap;
  }
  .email {
    position: absolute; left: 0; right: 0; top: 204px; text-align: center;
    font-family: Arial, sans-serif; font-size: 11px; letter-spacing: 0.5px;
  }
  .tagline {
    position: absolute; left: 0; right: 0; top: 258px; text-align: center;
    font-size: 17px; letter-spacing: 3px;
  }
  .field-photo {
    position: absolute; inset: 0;
    background: linear-gradient(180deg, var(--field-sky) 0%, #d9d6a8 35%, var(--field-wheat) 60%, var(--field-soil) 100%);
  }
  .services { position: absolute; }
  .services h2 { font-size: 26px; letter-spacing: 1px; font-weight: normal; line-height: 1.1; }
  .services ul { list-style: none; font-size: 14px; letter-spacing: 1.5px; line-height: 1.25; margin-top: 4px; }
  .services--earthmoving { left: 34px; top: 112px; }
  .services--transport { right: 32px; top: 40px; }
</style>
</head>
<body>
<main class="canvas">

  <section class="card card--front" aria-label="Business card front">
    <div class="dotted" style="top:96px; left:290px;"></div>
    <div class="business-name">RT Hadley Contracting</div>
    <div class="contact">
      <div class="phone">0400 555 123</div>
      <div class="address">42 Kurrajong Street<br>Millbrook 2899</div>
    </div>
    <div class="dotted" style="top:168px;"></div>
    <div class="name-pill">Russell Hadley</div>
    <div class="email">russhadley@example.com</div>
    <div class="dotted" style="top:236px;"></div>
    <div class="tagline">Earthmoving &amp; Transport Solutions</div>
    <div class="dotted" style="top:300px;"></div>
  </section>

  <section class="card card--back" aria-label="Business card back">
    <div class="field-photo" role="img" aria-label="Photo of a combine harvester working a wheat field"></div>
    <div class="dotted" style="top:24px;"></div>
    <div class="services services--earthmoving">
      <h2>Earthmoving</h2>
      <ul>
        <li>Road Building &amp; Maintenance</li>
        <li>Poly Pipe Laying</li>
        <li>Clearing fence lines</li>
        <li>Sand &amp; Gravel supplies</li>
      </ul>
    </div>
    <div class="services services--transport">
      <h2>Transport</h2>
      <ul>
        <li>Grain</li>
        <li>Cotton</li>
        <li>Sand &amp; Gravel</li>
        <li>Wool</li>
      </ul>
    </div>
    <div class="dotted" style="top:296px;"></div>
  </section>

</main>
</body>
</html>
```